Need a revamp of our website to attract larger companies and government authorities. The site must breathe that we are a company ready for larger projects both in the web and app sector. And also, that we can start projects with short notice.

Until now the design suggestions for us have been mor suitable for smaller firms but we have now taken the step in the larger/bigger range.

Most of our web nowadays has been work on digitalization of all kinds of administrative systems.

The site to be redone is https://brightvanta.eu And that brand is a sub brand to https://farmount.se

startpage
servicelist presentation page
service detail page
caselist page (same as article list)
case detail page (same as article detail)
about us page
contact us page
Updates

We have this video that can be used as a hero banner video

https://www.filecrate.example/t/9QkLm2ZpRtWvXyNb

Target Market(s)

b2b customers

Coding

Coded - Design and coding required

Number of Pages Required

5+ page

Font styles to use
Sans Serif

Requirements
Must have
• A thought throu theme. with details folowing the whole design www.outcomera.se
Nice to have
• maybe a video hero banner https://www.filecrate.example/t/9QkLm2ZpRtWvXyNb
Should not have
• a standard theme look and feel.

```html
<!DOCTYPE html>
<html lang="en">
<head>
<meta charset="utf-8">
<title>Bright Vanta — Web &amp; Mobile Apps</title>
<link href="https://fonts.googleapis.com/css2?family=Roboto:wght@300;400;500;700&family=Roboto+Condensed:wght@400&family=Lato:wght@400&family=Cinzel:wght@400&display=swap" rel="stylesheet">
<style>
:root{
  --navy:#0f1c2a;
  --slate:#2f4a5a;
  --slate-light:#4c6676;
  --ink:#1c2733;
  --grey-bg:#efefef;
  --text:#3a3f45;
  --blue:#1a6fd1;
  --star:#f6b51e;
  --white:#ffffff;
}
*{box-sizing:border-box;margin:0;padding:0}
html,body{width:1200px;height:3187px;overflow:hidden}
body{font-family:'Roboto',sans-serif;color:var(--ink);background:var(--white);position:relative}
.abs{position:absolute}
/* header */
.site-header{position:absolute;left:0;top:0;width:1200px;height:85px;background:var(--white)}
.brand{position:absolute;left:99px;top:22px;display:flex;align-items:center;gap:10px}
.brand-dot{width:36px;height:36px;border-radius:50%;background:var(--slate)}
.brand-name{font-size:17px;font-weight:500;letter-spacing:1.5px;color:var(--slate)}
.main-nav a{position:absolute;top:28px;font-size:18px;color:var(--ink);text-decoration:none}
.main-nav .active::before{content:"";position:absolute;left:-2px;right:-2px;top:-28px;height:3px;background:var(--slate)}
.phone-box{position:absolute;left:846px;top:19px;width:62px;height:43px;background:var(--navy);clip-path:polygon(14% 0,100% 0,86% 100%,0 100%)}
.phone-box svg{position:absolute;left:21px;top:12px}
.phone-number{position:absolute;left:923px;top:28px;font-size:20px;color:var(--slate)}
/* hero */
.hero{position:absolute;left:0;top:85px;width:1200px;height:646px;background:linear-gradient(180deg,#7a6c55 0%,#6e7a4a 40%,#5a7a3c 75%,#6a8a4a 100%)}
.hero-accent{position:absolute;left:700px;top:0;width:500px;height:646px;background:rgba(47,74,90,.72);clip-path:polygon(70% 0,100% 0,100% 30%,60% 100%,30% 100%)}
.hero h1{position:absolute;left:140px;top:84px;color:var(--white);line-height:1}
.hero .h-light{display:block;font-size:64px;font-weight:400}
.hero .h-bold{display:block;font-size:86px;font-weight:700;margin-top:4px}
.hero .tagline{position:absolute;left:142px;top:244px;font-size:26px;color:var(--white);font-weight:400}
.hero .lead{position:absolute;left:142px;top:294px;width:380px;font-size:15.5px;line-height:26px;color:var(--white)}
.pill-btn{position:absolute;height:50px;border-radius:25px;background:var(--navy);display:flex;align-items:center;gap:16px;padding:0 26px 0 4px;color:var(--white);font-size:16px;text-decoration:none}
.pill-btn .dot{width:42px;height:42px;border-radius:50%;background:var(--white);border:2px solid var(--slate)}
.play{position:absolute;left:698px;top:404px;width:180px;height:58px;border-radius:29px;background:rgba(47,74,90,.6);display:flex;align-items:center;gap:14px;padding-left:16px;color:var(--white);font-size:16px}
.play .circle{width:50px;height:50px;border-radius:50%;background:var(--white);display:flex;align-items:center;justify-content:center}
/* section heads */
.sec-mark{position:absolute;width:34px;height:28px;background:var(--slate);clip-path:polygon(30% 0,100% 0,70% 100%,0 100%)}
.sec-title{position:absolute;left:0;width:1200px;text-align:center;font-size:35px;color:var(--slate)}
.sec-title b{font-weight:700;color:var(--navy)}
.services-intro{position:absolute;left:210px;top:885px;width:780px;text-align:center;font-family:'Roboto Condensed',sans-serif;font-size:17px;line-height:26px;color:var(--ink)}
/* service cards */
.service-card{position:absolute;top:970px;width:244px;height:321px;color:var(--white);text-align:center}
.service-card.dark{background:var(--navy)}
.service-card.light{background:var(--slate)}
.service-icon{margin:25px auto 0;width:109px;height:109px;border-radius:50%;background:var(--white);border:5px solid var(--slate-light);display:flex;align-items:center;justify-content:center}
.service-card h3{font-weight:400;font-size:22px;margin-top:22px}
.service-card p{font-size:12.5px;line-height:19px;margin:10px 18px 0}
.learn-more{display:inline-block;margin-top:15px;width:102px;height:31px;border:1.5px solid var(--white);font-family:'Cinzel',serif;font-size:11px;line-height:28px;color:var(--white)}
/* about */
.about{position:absolute;left:0;top:1400px;width:1200px;height:412px;background:var(--grey-bg);overflow:hidden}
.about-photo{position:absolute;left:687px;top:0;width:513px;height:412px;background:linear-gradient(135deg,#c9b89a,#3e4a55 60%,#1f2a33);clip-path:polygon(45% 0,100% 0,100% 100%,0 100%,20% 40%)}
.about .kicker{position:absolute;left:136px;top:87px;font-size:36px;font-weight:300;color:var(--navy)}
.about h2{position:absolute;left:134px;top:138px;font-size:44px;font-weight:700;color:var(--slate)}
.about p{position:absolute;left:136px;top:208px;width:530px;font-family:'Lato',sans-serif;font-size:17px;line-height:26px;color:var(--text)}
/* clients */
.review-card{position:absolute;top:1999px;width:313px;height:285px;border:2px solid #d9dde1;border-radius:22px;background:var(--white)}
.quote-mark{position:absolute;left:20px;top:30px}
.review-card p{position:absolute;left:20px;top:76px;width:280px;font-size:15px;line-height:22.5px;color:#6a6f74}
.stars{position:absolute;left:18px;top:172px;display:flex;gap:3px}
.review-card .name{position:absolute;left:22px;top:202px;font-size:21px;color:var(--navy)}
.review-card .count{position:absolute;left:22px;top:235px;font-size:17px;color:var(--navy)}
.avatar{position:absolute;left:197px;top:238px;width:76px;height:76px;border-radius:50%;background:radial-gradient(circle at 40% 35%,#d9b89c,#6b5646)}
/* quote band */
.quote-band{position:absolute;left:0;top:2397px;width:1200px;height:403px;background:var(--blue);overflow:hidden}
.devices{position:absolute;left:0;top:0;width:620px;height:403px;background:linear-gradient(120deg,#1f8cf0 0%,#9aa3b0 45%,#2a78d6 100%);clip-path:polygon(0 20%,18% 0,60% 0,100% 30%,100% 100%,0 100%)}
.quote-band h2{position:absolute;left:684px;top:90px;font-size:34px;line-height:38px;font-weight:700;color:var(--white)}
.quote-band p{position:absolute;left:687px;top:200px;width:420px;font-size:17px;line-height:26px;color:var(--white)}
/* footer */
.site-footer{position:absolute;left:0;top:2800px;width:1200px;height:387px;background:var(--navy);color:var(--white)}
.footer-brand-dot{position:absolute;left:195px;top:100px;width:95px;height:95px;border-radius:50%;background:var(--white)}
.footer-brand{position:absolute;left:96px;top:220px;font-size:36px;font-weight:500;letter-spacing:3px}
.footer-col h4{position:absolute;top:84px;font-size:16px;font-weight:700}
.footer-col a{position:absolute;font-size:15px;color:var(--white);text-decoration:none}
.newsletter h4{position:absolute;left:841px;top:84px;width:260px;font-size:16px;font-weight:700;line-height:20px}
.newsletter p{position:absolute;left:845px;top:136px;width:240px;font-size:11.5px;line-height:20px}
.email-field{position:absolute;left:846px;top:203px;width:230px;height:35px;border:1px solid var(--white);border-radius:4px;font-size:11px;padding:10px 12px}
.email-field .sep{position:absolute;left:193px;top:6px;width:1px;height:22px;background:var(--white)}
.email-field svg{position:absolute;left:204px;top:10px}
.consent-box{position:absolute;left:847px;top:256px;width:16px;height:14px;border:1px solid var(--white);border-radius:3px}
.consent{position:absolute;left:879px;top:252px;width:210px;font-size:11.5px;line-height:17px}
.footer-rule{position:absolute;left:111px;top:312px;width:978px;height:1px;background:#6d7a86}
.copyright{position:absolute;left:380px;top:340px;font-size:17px}
.parent-brand{position:absolute;left:920px;top:335px;font-size:24px;font-weight:300;letter-spacing:1px}
</style>
</head>
<body>

<header class="site-header">
  <div class="brand"><span class="brand-dot"></span><span class="brand-name">BRIGHT VANTA</span></div>
  <nav class="main-nav">
    <a class="active" style="left:323px">Home</a>
    <a style="left:403px">About Us</a>
    <a style="left:507px">Services</a>
    <a style="left:605px">Case</a>
    <a style="left:678px">Contact Us</a>
  </nav>
  <div class="phone-box"><svg width="20" height="20" viewBox="0 0 24 24" fill="#fff"><path d="M6.6 10.8a15.1 15.1 0 0 0 6.6 6.6l2.2-2.2a1 1 0 0 1 1-.25 11.4 11.4 0 0 0 3.6.57 1 1 0 0 1 1 1V20a1 1 0 0 1-1 1A17 17 0 0 1 3 4a1 1 0 0 1 1-1h3.5a1 1 0 0 1 1 1c0 1.25.2 2.45.57 3.57a1 1 0 0 1-.25 1z"/></svg></div>
  <div class="phone-number">+46 (0)40 555 01 23</div>
</header>

<section class="hero" role="img" aria-label="Aerial view of a harvester working a green field">
  <div class="hero-accent"></div>
  <h1><span class="h-light">BRIGHT</span><span class="h-bold">VANTA</span></h1>
  <div class="tagline">Web &amp; Mobile Apps</div>
  <p class="lead">Located in Sweden we have provided software since 1999. With our experts in areas like web development and mobile app development, we provide first-class software and project management.</p>
  <a class="pill-btn" style="left:142px;top:425px"><span class="dot"></span>Render Quote</a>
  <div class="play"><span class="circle"><svg width="18" height="20" viewBox="0 0 18 20"><path d="M2 1l15 9-15 9z" fill="#0f1c2a"/></svg></span>Play video</div>
</section>

<section class="services">
  <span class="sec-mark" style="left:583px;top:804px"></span>
  <h2 class="sec-title" style="top:834px;font-weight:400">SOME OF <b>OUR SERVICES</b></h2>
  <p class="services-intro">Bright Vanta® provide senior resources in a vast range of areas within system development. Lately, most of our work has been within the fields of app and web development.</p>

  <article class="service-card dark" style="left:99px">
    <div class="service-icon"><svg width="60" height="60" viewBox="0 0 60 60" fill="none" stroke="#1c2733" stroke-width="2.5"><circle cx="28" cy="32" r="24"/><circle cx="28" cy="32" r="16"/><circle cx="28" cy="32" r="8"/><path d="M28 32L52 8M46 6l6 2 2 6"/></svg></div>
    <h3>Web development</h3>
    <p>Entertain our readers’ intellectual and cultural appetite and their sophisticated needs content.</p>
    <span class="learn-more">LEARN MORE</span>
  </article>
  <article class="service-card light" style="left:351px">
    <div class="service-icon"><svg width="60" height="60" viewBox="0 0 60 60" fill="none" stroke="#1c2733" stroke-width="2.5"><circle cx="16" cy="12" r="5"/><circle cx="30" cy="10" r="5"/><circle cx="44" cy="12" r="5"/><path d="M8 28c0-6 16-6 16 0M22 26c0-6 16-6 16 0M36 28c0-6 16-6 16 0M6 44l12-6h14l-4 5h-8M18 52l8-4h14l14-10"/></svg></div>
    <h3>Post-Launch Support</h3>
    <p>Entertain our readers’ intellectual and cultural appetite and their sophisticated needs content.</p>
    <span class="learn-more">LEARN MORE</span>
  </article>
  <article class="service-card dark" style="left:604px">
    <div class="service-icon"><svg width="60" height="60" viewBox="0 0 60 60" fill="none" stroke="#1c2733" stroke-width="2.5"><path d="M10 50V36M20 50V28M30 50V32M40 50V22M50 50V30M6 52h48"/><circle cx="40" cy="12" r="6"/><path d="M14 30l10-8 10 4 8-10"/></svg></div>
    <h3>Design and UX</h3>
    <p>Entertain our readers’ intellectual and cultural appetite and their sophisticated needs content.</p>
    <span class="learn-more">LEARN MORE</span>
  </article>
  <article class="service-card light" style="left:856px">
    <div class="service-icon"><svg width="60" height="60" viewBox="0 0 60 60" fill="none" stroke="#1c2733" stroke-width="2.5"><path d="M6 50l18-26 8 10 6-6 16 22z"/><path d="M26 24V6h12l-3 4 3 4H26"/></svg></div>
    <h3>App development</h3>
    <p>Entertain our readers’ intellectual and cultural appetite and their sophisticated needs content.</p>
    <span class="learn-more">LEARN MORE</span>
  </article>
</section>

<section class="about">
  <div class="about-photo" role="img" aria-label="Businessman in a suit talking on the phone in an office"></div>
  <span class="sec-mark" style="left:136px;top:50px"></span>
  <div class="kicker">ABOUT US</div>
  <h2>BRIGHT VANTA®</h2>
  <p>Bright Vanta® is all about creating software smarter by providing a senior expert in each area of the project. With our long experience, we know how to make software better, smarter and faster.</p>
  <a class="pill-btn" style="left:138px;top:313px;font-size:17px"><span class="dot"></span>Read More</a>
</section>

<section class="clients">
  <span class="sec-mark" style="left:583px;top:1884px"></span>
  <h2 class="sec-title" style="top:1926px;font-weight:700;color:var(--navy)">SOME OF OUR CLIENTS</h2>

  <article class="review-card" style="left:99px">
    <svg class="quote-mark" width="30" height="24" viewBox="0 0 30 24" fill="#2f4a5a"><path d="M0 24V12C0 5 4 1 11 0v5c-3 1-5 3-5 6h5v13zM17 24V12c0-7 4-11 11-12v5c-3 1-5 3-5 6h5v13z"/></svg>
    <p>Lorem ipsum dolor sit amet, consectetur adipiscing elit, sed do eiusmod tempor incididunt ut labore et dolore magna aliqua.</p>
    <div class="stars"><svg width="100" height="18" viewBox="0 0 100 18" fill="#f6b51e"><path id="s" d="M9 0l2.7 5.8 6.3.7-4.7 4.3 1.3 6.2L9 13.9 3.4 17l1.3-6.2L0 6.5l6.3-.7z"/><use href="#s" x="20"/><use href="#s" x="40"/><use href="#s" x="60"/><use href="#s" x="80"/></svg></div>
    <div class="name">Mira Holt</div><div class="count">10 reviews</div>
    <div class="avatar" role="img" aria-label="Client portrait"></div>
  </article>
  <article class="review-card" style="left:441px">
    <svg class="quote-mark" width="30" height="24" viewBox="0 0 30 24" fill="#2f4a5a"><path d="M0 24V12C0 5 4 1 11 0v5c-3 1-5 3-5 6h5v13zM17 24V12c0-7 4-11 11-12v5c-3 1-5 3-5 6h5v13z"/></svg>
    <p>Lorem ipsum dolor sit amet, consectetur adipiscing elit, sed do eiusmod tempor incididunt ut labore et dolore magna aliqua.</p>
    <div class="stars"><svg width="100" height="18" viewBox="0 0 100 18" fill="#f6b51e"><use href="#s"/><use href="#s" x="20"/><use href="#s" x="40"/><use href="#s" x="60"/><use href="#s" x="80"/></svg></div>
    <div class="name">Jonas Berg</div><div class="count">8 reviews</div>
    <div class="avatar" role="img" aria-label="Client portrait"></div>
  </article>
  <article class="review-card" style="left:783px">
    <svg class="quote-mark" width="30" height="24" viewBox="0 0 30 24" fill="#2f4a5a"><path d="M0 24V12C0 5 4 1 11 0v5c-3 1-5 3-5 6h5v13zM17 24V12c0-7 4-11 11-12v5c-3 1-5 3-5 6h5v13z"/></svg>
    <p>Lorem ipsum dolor sit amet, consectetur adipiscing elit, sed do eiusmod tempor incididunt ut labore et dolore magna aliqua.</p>
    <div class="stars"><svg width="100" height="18" viewBox="0 0 100 18" fill="#f6b51e"><use href="#s"/><use href="#s" x="20"/><use href="#s" x="40"/><use href="#s" x="60"/><use href="#s" x="80"/></svg></div>
    <div class="name">Elin Sandvik</div><div class="count">2 reviews</div>
    <div class="avatar" role="img" aria-label="Client portrait"></div>
  </article>
</section>

<section class="quote-band">
  <div class="devices" role="img" aria-label="Laptop, tablet and monitor showing a website design"></div>
  <h2>BRIGHT VANTA®<br>REQUEST FOR QUOTE</h2>
  <p>Start the exciting journey of creating a mobile app or website by submitting a request for a quote. Requests are handled quickly and with integrity.</p>
  <a class="pill-btn" style="left:684px;top:302px;height:48px"><span class="dot" style="width:40px;height:40px"></span>Render Quote</a>
</section>

<footer class="site-footer">
  <div class="footer-brand-dot"></div>
  <div class="footer-brand">BRIGHT VANTA</div>

  <div class="footer-col">
    <h4 style="left:429px">QUICK LINKS</h4>
    <a style="left:434px;top:140px">Home</a>
    <a style="left:434px;top:173px">About Us</a>
    <a style="left:434px;top:206px">Services</a>
    <a style="left:434px;top:240px">Case</a>
    <a style="left:434px;top:273px">Contact Us</a>
  </div>
  <div class="footer-col">
    <h4 style="left:607px">PURCHASE</h4>
    <a style="left:612px;top:140px">Delivery Policy</a>
    <a style="left:612px;top:173px">Data Policy</a>
    <a style="left:612px;top:206px">Refund Policy</a>
    <a style="left:612px;top:240px">Charges And Fees</a>
  </div>
  <div class="newsletter">
    <h4>WANT TO BE UPDATED ABOUT BRIGHT VANTA?</h4>
    <p>Sign up for the Bright Vanta newsletter and get the latest news and offers sent directly to your inbox.</p>
    <div class="email-field">Email *<span class="sep"></span><svg width="14" height="14" viewBox="0 0 24 24" fill="#fff"><path d="M2 21l21-9L2 3v7l15 2-15 2z"/></svg></div>
    <span class="consent-box"></span>
    <div class="consent">I agree to receive other communications from Bright Vanta.</div>
  </div>
  <div class="footer-rule"></div>
  <div class="copyright">© copyrights 2022 Bright Vanta |&nbsp; All Rights Reserved</div>
  <div class="parent-brand">farmount ab</div>
</footer>

</body>
</html>
```